Lumokrit alias Jarek hat fantastische Arbeit geleistet. Zeitnahe Kommunikation, zeitnahe Umsetzung des Feedbacks und zeitnahe Bereitstellung des fertigen Projektes. Gerne jederzeit wieder.
Zielgruppe
Onlinemarketing Services für kleine und mittlere Unternehmen, wie z.B. Webseitenbau, Social Media Kampagnen oder Suchmaschinenoptimierung. Zu unseren Kunden gehören Handwerker, Tierärzte, Rechtsanwälte oder Kfz-Meisterbetriebe. Wir bedienen 6.000 Branchen von Aalräucherei bis Zylinderschleiferei, fokussieren uns aber stark auf das Handwerk.
Aufgabenstellung
Wir planen unsere Produkte unseren Kunden auf einer Plattform zur Verfügung zustellen. Hier sollen sie sich einloggen können und die Self und Managed Services nutzen können. Wir benötigen dafür eine Visualisierung. Also keine echte Webseite, sondern eine Anmutung. Sie soll nicht klickbar sein, aber sich schon wie eine fertige Webseite anfühlen.
Insgesamt sollen 3 Unterseiten gestaltet werden, die wir bereits skizziert (siehe Mockups) haben. Wir sind offen für deine Gestaltungsideen, Hauptsache es sieht nach was aus. Uns ist zudem wichtig, dass du dich bei der Farbgestaltung an der Webseite www.falvoria.com orientierst (Faust-Icon, Logo und Farbe).

```html
<!DOCTYPE html>
<html lang="de">
<head>
<meta charset="utf-8">
<title>falvoria.com – Marketing & Recruiting für Handwerker</title>
<link href="https://fonts.googleapis.com/css2?family=Open+Sans:wght@400;600;700&display=swap" rel="stylesheet">
<style>
  :root {
    --orange: #ec7a08;
    --text: #1d1d1d;
    --muted: #8a8a8a;
    --bg: #f7f7f7;
    --band: #f1f1f1;
    --card: #ffffff;
  }
  * { box-sizing: border-box; margin: 0; padding: 0; }
  html, body { width: 1039px; height: 1200px; overflow: hidden; }
  body { background: var(--bg); font-family: 'Open Sans', sans-serif; color: var(--text); position: relative; }
  .abs { position: absolute; }

  .brand { left: 82px; top: 12px; display: flex; align-items: center; gap: 8px; }
  .brand-dot { width: 38px; height: 38px; border-radius: 50%; background: var(--orange); }
  .brand-name { font-size: 23px; font-weight: 600; color: #4a4a4a; }

  .nav { top: 29px; font-size: 10.5px; letter-spacing: .3px; }
  .nav a { position: absolute; color: var(--text); text-decoration: none; white-space: nowrap; }
  .nav a.active { color: var(--orange); font-weight: 700; }

  .btn { display: flex; align-items: center; justify-content: center; border-radius: 20px; font-size: 11px; white-space: nowrap; }
  .btn-solid { background: var(--orange); color: #fff; }
  .btn-line { border: 1.5px solid var(--orange); color: var(--orange); background: transparent; }
  .btn-big { font-size: 13.5px; border-radius: 24px; }

  .hero-title { left: 85px; top: 152px; font-size: 30px; line-height: 36px; font-weight: 700; color: var(--orange); }
  .hero-text { left: 85px; top: 236px; width: 340px; font-size: 13px; line-height: 18px; }
  .hero-text p + p { margin-top: 8px; }
  .hero-photo { left: 469px; top: 102px; width: 487px; height: 365px; border-radius: 10px;
    background: linear-gradient(135deg, #7b6a58 0%, #a99583 35%, #4f5663 65%, #8b5a45 100%);
    box-shadow: 0 2px 6px rgba(0,0,0,.25); }

  .card { top: 512px; width: 280px; height: 257px; background: var(--card); box-shadow: 0 1px 4px rgba(0,0,0,.18); }
  .card h3 { position: absolute; left: 18px; top: 10px; font-size: 15px; font-weight: 700; color: var(--orange); }
  .item { position: absolute; left: 14px; display: flex; gap: 22px; align-items: center; }
  .thumb { width: 108px; height: 65px; flex: none; }
  .item p { font-size: 9.5px; line-height: 11.8px; color: var(--muted); width: 130px; white-space: nowrap; }
  .card .btn { position: absolute; left: 88px; top: 216px; width: 110px; height: 22px; border: 1.5px solid #333; color: #333; font-size: 11px; }

  .band { left: 0; top: 813px; width: 1039px; height: 387px; background: var(--band); }
  .section-title { left: 0; top: 868px; width: 1039px; text-align: center; font-size: 23px; line-height: 30px; font-weight: 700; color: var(--orange); }
  .feature { top: 938px; width: 180px; text-align: center; }
  .feature svg { display: block; margin: 0 auto; width: 100px; height: 96px; }
  .feature span { display: block; margin-top: 12px; font-size: 15px; line-height: 19px; font-weight: 700; }
</style>
</head>
<body>
  <div class="abs brand"><div class="brand-dot"></div><span class="brand-name">falvoria.com</span></div>

  <nav class="abs nav" style="left:0">
    <a class="active" style="left:335px">START</a>
    <a style="left:400px">SERVICES</a>
    <a style="left:485px">FUNKTIONEN</a>
    <a style="left:590px">PREISE</a>
  </nav>
  <div class="abs btn btn-solid" style="left:702px;top:24px;width:116px;height:22px">Kostenlos testen!</div>
  <div class="abs btn btn-line" style="left:828px;top:24px;width:128px;height:22px">Mein Falvoria.com</div>

  <h1 class="abs hero-title">Marketing &amp; Recruiting<br>für Handwerker</h1>
  <div class="abs hero-text">
    <p>Wir gestalten das Handwerk von morgen - mit<br>digitalen Lösungen für Deine Betriebsführung.</p>
    <p>Werde online sichtbar und positioniere Dich als<br>erfolgreicher Betrieb und attraktiver Arbeitgeber.</p>
  </div>
  <div class="abs btn btn-solid btn-big" style="left:85px;top:336px;width:179px;height:34px">Kostenlos testen!</div>
  <div class="abs hero-photo" role="img" aria-label="Lächelnder Handwerker mit Gehörschutz arbeitet in einer Werkstatt am Laptop"></div>

  <section class="abs card" style="left:85px">
    <h3>Branchen-News</h3>
    <div class="item" style="top:48px"><div class="thumb" role="img" aria-label="Pickup fährt durch ein Feld" style="background:linear-gradient(135deg,#5d6b3c,#c9c4b6,#7a6a44)"></div><p>Lorem ipsum dolor sit<br>amet, conjest consec<br>tetuer adiscing elit Aenean<br>commodo est.</p></div>
    <div class="item" style="top:130px"><div class="thumb" role="img" aria-label="Handwerker montieren Solarmodule auf einem Dach" style="background:linear-gradient(135deg,#c8a46a,#e8eef2,#3b4f66)"></div><p>Lorem ipsum dolor sit<br>amet, conjest consec<br>tetuer adiscing elit Aenean<br>commodo est.</p></div>
    <div class="btn">Zur Übersicht</div>
  </section>

  <section class="abs card" style="left:378px">
    <h3>Fortbildung</h3>
    <div class="item" style="top:48px"><div class="thumb" role="img" aria-label="Handwerker installiert ein Solarmodul" style="background:linear-gradient(135deg,#4a5fa0,#c94a3a,#7a4a3a)"></div><p>Lorem ipsum dolor sit<br>amet, conjest consec<br>tetuer adiscing elit Aenean<br>commodo est.</p></div>
    <div class="item" style="top:130px"><div class="thumb" role="img" aria-label="Handwerker montieren Solarmodule auf einem Dach" style="background:linear-gradient(135deg,#c8a46a,#e8eef2,#3b4f66)"></div><p>Lorem ipsum dolor sit<br>amet, conjest consec<br>tetuer adiscing elit Aenean<br>commodo est.</p></div>
    <div class="btn">Zur Übersicht</div>
  </section>

  <section class="abs card" style="left:672px">
    <h3>Jobs</h3>
    <div class="item" style="top:48px"><div class="thumb" role="img" aria-label="Techniker arbeitet an einer Wärmepumpe" style="background:linear-gradient(135deg,#9aa0a6,#e3e5e7,#5a5f66)"></div><p>Lorem ipsum dolor sit<br>amet, conjest consec<br>tetuer adiscing elit Aenean<br>commodo est.</p></div>
    <div class="item" style="top:130px"><div class="thumb" role="img" aria-label="Handwerker montieren Solarmodule auf einem Dach" style="background:linear-gradient(135deg,#c8a46a,#e8eef2,#3b4f66)"></div><p>Lorem ipsum dolor sit<br>amet, conjest consec<br>tetuer adiscing elit Aenean<br>commodo est.</p></div>
    <div class="btn">Zur Übersicht</div>
  </section>

  <div class="abs band"></div>
  <h2 class="abs section-title">Wir machen Dich fit für die digitale Betriebsführung</h2>

  <div class="abs feature" style="left:62px">
    <svg viewBox="0 0 100 96" fill="none" stroke="#111" stroke-width="2.5" stroke-linejoin="round">
      <path d="M20 8h76v74H14a6 6 0 0 1-6-6V26h12"/><path d="M20 8v68a6 6 0 0 1-6 6"/>
      <rect x="28" y="20" width="22" height="10"/><path d="M56 20h32M56 30h32M28 40h60M28 50h60M28 60h60M28 70h60"/>
    </svg>
    <span>Branchen-News<br>erhalten</span>
  </div>
  <div class="abs feature" style="left:231px">
    <svg viewBox="0 0 100 96" fill="none" stroke="#111" stroke-width="2.5" stroke-linejoin="round">
      <path d="M8 22h84v34H8z"/><path d="M14 56v32h72V56"/><path d="M30 22a20 12 0 0 1 40 0"/>
      <path d="M10 16h14M76 16h14"/><rect x="44" y="48" width="12" height="16" rx="6"/>
    </svg>
    <span>Fachpersonal<br>finden</span>
  </div>
  <div class="abs feature" style="left:410px">
    <svg viewBox="0 0 100 96" fill="none" stroke="#111" stroke-width="2.5" stroke-linecap="round">
      <ellipse cx="48" cy="24" rx="16" ry="19"/><path d="M40 42v6L18 64a8 8 0 0 0 4 14h44"/><path d="M56 42v6l10 8"/>
      <path d="M80 66v20M70 76h20"/>
    </svg>
    <span>Kunden<br>gewinnen</span>
  </div>
  <div class="abs feature" style="left:599px">
    <svg viewBox="0 0 100 96" fill="none" stroke="#111" stroke-width="2.5" stroke-linejoin="round" stroke-linecap="round">
      <path d="M50 40L34 24a10 10 0 0 1 16-14 10 10 0 0 1 16 14z"/>
      <path d="M10 80l10-18 12-12 22 2a5 5 0 0 1 0 10H40"/><path d="M54 62l24-18a6 6 0 0 1 8 8L64 78l-38 10z"/>
    </svg>
    <span>Kundenbeziehungen<br>stärken</span>
  </div>
  <div class="abs feature" style="left:792px">
    <svg viewBox="0 0 100 96" fill="none" stroke="#111" stroke-width="2.5" stroke-linejoin="round">
      <rect x="42" y="4" width="56" height="40"/><rect x="48" y="10" width="44" height="28"/>
      <path d="M62 14h10l6 6v14H62z"/><path d="M70 44v8M58 54h24"/>
      <path d="M18 42V28h8M22 24l4 4-4 4"/>
      <path d="M4 62l16-8 16 8-16 8z"/><path d="M4 70l16 8 16-8M4 78l16 8 16-8"/>
    </svg>
    <span>Betrieb<br>digitalisieren</span>
  </div>

  <div class="abs btn btn-solid btn-big" style="left:433px;top:1123px;width:178px;height:34px">Kostenlos testen!</div>
</body>
</html>
```